Fact Sheets for Insurance

We need a 4 page booklet brochure designed for our insurance business. Each page is A4. We design insurance plans for our Clients and we wish to use the brochure to market and educate our Client and business partners. The business is Halvorsen Brightwick Financial Services. Colour scheme of our logo and stationary is navy blue and metallic gold. The content has been drafted and each page is attached. Please use your creative freedom to make it look professional and modern. We would like graphics, pictures etc to make it more vibrant as well.

Industry/Entity Type

Insurance

```html
<!DOCTYPE html>
<html lang="en">
<head>
<meta charset="utf-8">
<title>Insurance Fact Sheets – Halvorsen Brightwick Financial Services</title>
<link href="https://fonts.googleapis.com/css2?family=Open+Sans:ital,wght@0,400;0,700;1,400;1,700&family=Tinos:wght@700&display=swap" rel="stylesheet">
<style>
  :root{
    --stage:#a7a9ac;
    --navy:#1d3f6e;
    --navy-deep:#17345c;
    --gold:#b5a77f;
    --gold-dot:#c7b47a;
    --ink:#1d2b40;
    --row:#e6e8ec;
    --row-head:#c9ccd1;
    --white:#ffffff;
  }
  *{box-sizing:border-box;margin:0;padding:0}
  html,body{width:1200px;height:1000px;overflow:hidden;background:var(--stage)}
  body{position:relative;font-family:"Open Sans",Arial,sans-serif;color:var(--white)}

  /* ---------- main sheet ---------- */
  .sheet{position:absolute;left:120px;top:10px;width:692px;height:980px;background:var(--navy)}
  .sheet-title{height:70px;display:flex;align-items:center;justify-content:center;
    font-family:"Tinos",serif;font-weight:700;font-size:19px;letter-spacing:.3px}
  .hero{height:213px;background:linear-gradient(100deg,#e9e9e7 0%,#bdbdbb 30%,#4a4b4d 55%,#222 75%,#6d6e70 100%)}
  .band{position:absolute;left:0;width:100%;background:var(--gold);color:var(--navy-deep);
    font-family:"Tinos",serif;font-weight:700;text-align:center;font-size:15px;line-height:26px;height:26px;letter-spacing:.3px}
  .need-table{position:absolute;left:74px;top:326px;width:544px;border-collapse:collapse;font-size:13px;color:var(--ink)}
  .need-table th{background:var(--row-head);font-weight:700;height:17px;line-height:15px;border:1px solid var(--navy)}
  .need-table td{background:var(--row);height:17.5px;line-height:15px;border:1px solid var(--navy);padding:0 8px}
  .need-table td:first-child{width:272px;padding-left:64px}
  .need-table .total td:first-child{text-align:right;font-weight:700}
  .offer-list{position:absolute;left:47px;top:464px;width:640px;list-style:none;font-size:14px;display:grid;
    grid-template-columns:205px 198px 220px;row-gap:7px}
  .dot li,.offer-list li{position:relative;padding-left:13px}
  .offer-list li::before,.help-list li::before{content:"";position:absolute;left:0;top:7px;width:6px;height:6px;border-radius:50%;background:var(--gold-dot)}
  .tips{position:absolute;left:50px;top:548px;width:620px;list-style:none;font-size:13.5px;line-height:17px}
  .tips li{position:relative;padding-left:24px;margin-bottom:4px}
  .tips svg{position:absolute;left:0;top:1px}
  .help-intro{position:absolute;left:53px;top:716px;font-size:14.5px}
  .help-list{position:absolute;left:60px;top:735px;list-style:none;font-size:14px;line-height:21.5px}
  .help-list li{position:relative;padding-left:14px}
  .help-outro{position:absolute;left:53px;top:821px;font-size:14px}
  .disclaimer{position:absolute;left:32px;top:857px;width:630px;font-size:8.6px;font-style:italic;line-height:12px}
  .brand{position:absolute;left:0;width:100%;text-align:center;font-family:"Open Sans",sans-serif;font-weight:400;color:var(--white)}
  .sheet .brand{top:922px;font-size:16px;line-height:20px;letter-spacing:1.5px}

  /* ---------- mini sheets ---------- */
  .mini{position:absolute;left:855px;width:226px;height:318px;background:var(--navy);overflow:hidden}
  .mini-title{height:22px;line-height:24px;text-align:center;font-family:"Tinos",serif;font-weight:700;font-size:9.5px}
  .mini-photo{height:73px}
  .mini-band{background:var(--gold);color:var(--navy-deep);font-family:"Tinos",serif;font-weight:700;
    font-size:4.5px;text-align:center;height:7px;line-height:7px;margin-top:4px}
  .mini-table{margin:3px 0 0 24px;width:178px;border-collapse:collapse;font-size:4.5px;color:var(--ink)}
  .mini-table th{background:var(--row-head);height:5px;line-height:5px;border:.5px solid var(--navy)}
  .mini-table td{background:var(--row);height:5px;line-height:5px;border:.5px solid var(--navy);padding:0 2px}
  .mini-table td:first-child{width:89px;padding-left:21px}
  .mini-table .total td:first-child{text-align:right;font-weight:700}
  .mini-offers{display:grid;grid-template-columns:68px 64px 70px;list-style:none;font-size:4.4px;margin:3px 0 0 18px;row-gap:2px}
  .mini-offers li::before,.mini-help li::before{content:"• ";color:var(--gold-dot)}
  .mini-text{font-size:4.2px;line-height:6px;padding:0 14px;margin-top:3px}
  .mini-tips{list-style:none;font-size:4.2px;line-height:5.6px;margin:3px 14px 0 14px}
  .mini-tips li{padding-left:7px;position:relative;margin-bottom:1px}
  .mini-tips li::before{content:"✓";position:absolute;left:0;color:#d8e0ea}
  .mini-help{list-style:none;font-size:4.2px;line-height:6px;margin-left:22px}
  .mini-disc{font-size:3.2px;font-style:italic;line-height:4.4px;padding:0 14px;margin-top:5px}
  .mini .brand{position:static;font-size:5.5px;letter-spacing:.6px;line-height:7px;margin-top:8px}
</style>
</head>
<body>

<main class="sheet">
  <h1 class="sheet-title">BUYING TOTAL &amp; PERMANENT DISABILITY (TPD) INSURANCE</h1>
  <div class="hero" role="img" aria-label="Photo of a hand resting on the wheel of a wheelchair"></div>

  <div class="band" style="top:295px">HOW MUCH DO I NEED?</div>
  <table class="need-table">
    <tr><th>Need</th><th>Amount</th></tr>
    <tr><td>Repaying Debts</td><td>$</td></tr>
    <tr><td>Medical Expenses</td><td>$</td></tr>
    <tr><td>Home Modification Costs</td><td>$</td></tr>
    <tr><td>Others</td><td>$</td></tr>
    <tr class="total"><td>Total</td><td>$</td></tr>
  </table>

  <div class="band" style="top:436px">WHO OFFERS IT?</div>
  <ul class="offer-list">
    <li>Most Superannuation Funds</li><li>Some Employers</li><li>General Insurance Companies</li>
    <li>Some Private Health Funds</li><li>Life Insurance Companies</li>
  </ul>

  <div class="band" style="top:518px">TIPS AND TRAPS</div>
  <ul class="tips">
    <li><svg width="16" height="14" viewBox="0 0 16 14"><path d="M1 8l4 4L15 1" fill="none" stroke="#c8d3e2" stroke-width="2"/></svg><b>Purchase an "Own Occupation" definition Policy</b> to ensure that you are not tested against your ability to work in "Any Occupation" at claim time.</li>
    <li><svg width="16" height="14" viewBox="0 0 16 14"><path d="M1 8l4 4L15 1" fill="none" stroke="#c8d3e2" stroke-width="2"/></svg><b>Review what the policy doesn't cover "Exclusions"</b>. Standard exclusion for most policies is self-inflicted acts.</li>
    <li><svg width="16" height="14" viewBox="0 0 16 14"><path d="M1 8l4 4L15 1" fill="none" stroke="#c8d3e2" stroke-width="2"/></svg>Look to <b>purchase "Long Term" Life Insurance</b> if you think you will need to hold the policy for a number of years. This may save you tens of thousands of dollars over the life of your policy.</li>
    <li><svg width="16" height="14" viewBox="0 0 16 14"><path d="M1 8l4 4L15 1" fill="none" stroke="#c8d3e2" stroke-width="2"/></svg>Ensure the contract is <b>guaranteed to be renewed</b> if you pay your premiums until expiry age.</li>
  </ul>

  <div class="band" style="top:687px">WHEN TO CALL A PROFESSIONAL ADVISOR?</div>
  <p class="help-intro">If you need help:</p>
  <ul class="help-list">
    <li>Comparing premiums</li>
    <li>Reviewing &amp; comparing policy terms and conditions</li>
    <li>Matching a policy to suit your occupation</li>
    <li>Purchasing “Long Term” Life Insurance</li>
  </ul>
  <p class="help-outro">If you want to ensure that you have someone assisting you if a claim is ever needed to be made</p>

  <p class="disclaimer">The information provided on this Fact Sheet is <b>general advice only</b> so does <b>not</b> take into account your objective, financial situation and needs. Before acting on any information contained on this Fact Sheet you should consider the appropriateness of the advice having regard to your own objectives, financial situation and needs.</p>
  <p class="brand">Halvorsen Brightwick<br>Financial Services</p>
</main>

<section class="mini" style="top:10px">
  <h2 class="mini-title">BUYING CRITICAL ILLNESS INSURANCE</h2>
  <div class="mini-photo" role="img" aria-label="Photo of a doctor with a stethoscope" style="background:linear-gradient(90deg,#f4f5f7,#dfe3ea 55%,#2c4f86 75%,#f1f2f4)"></div>
  <div class="mini-band">HOW MUCH DO I NEED?</div>
  <table class="mini-table">
    <tr><th>Need</th><th>Amount</th></tr>
    <tr><td>Medical Expenses</td><td>$</td></tr>
    <tr><td>Others</td><td>$</td></tr>
    <tr class="total"><td>Total</td><td>$</td></tr>
  </table>
  <div class="mini-band">WHO OFFERS IT?</div>
  <ul class="mini-offers"><li>Some Private Health Funds</li><li>Life Insurance Companies</li><li></li><li>Some Employers</li><li>General Insurance Companies</li></ul>
  <div class="mini-band">TIPS AND TRAPS</div>
  <ul class="mini-tips">
    <li><b>Pay particular attention to the definitions for Cancer and Cardiovascular conditions</b> such as Heart Attack so you are aware of when you can claim.</li>
    <li><b>Review what the policy doesn't cover "Exclusions"</b>. Standard exclusion for most policies is self-inflicted acts.</li>
    <li>Look to <b>purchase "Long Term" Life Insurance</b> if you think you will need to hold the policy for a number of years. This may save you tens of thousands of dollars over the life of your policy.</li>
    <li>Ensure the contract is <b>guaranteed to be renewed</b> if you pay your premiums until expiry age.</li>
  </ul>
  <div class="mini-band">WHEN TO CALL A PROFESSIONAL ADVISOR?</div>
  <p class="mini-text">If you need help:</p>
  <ul class="mini-help"><li>Comparing premiums</li><li>Reviewing &amp; comparing policy terms and conditions</li><li>Purchasing "Long Term" Life Insurance</li></ul>
  <p class="mini-text" style="margin-top:0">If you want to ensure that you have someone assisting you if a claim is ever needed to be made</p>
  <p class="mini-disc">The information provided on this Fact Sheet is general advice only so does not take into account your objective, financial situation and needs. Before acting on any information you should consider its appropriateness to your own objectives, financial situation and needs.</p>
  <p class="brand">Halvorsen Brightwick<br>Financial Services</p>
</section>

<section class="mini" style="top:340px">
  <h2 class="mini-title">BUYING INCOME PROTECTION INSURANCE</h2>
  <div class="mini-photo" role="img" aria-label="Photo of colourful banknotes" style="background:linear-gradient(100deg,#3a7fb8,#e7a25a 35%,#e9d37a 55%,#d86a3e 75%,#4f9b86)"></div>
  <div class="mini-band">HOW MUCH DO I NEED?</div>
  <p class="mini-text">Most people insure 75% of their income, which is the maximum benefit that Insurance Companies generally cover.</p>
  <div class="mini-band">WHO OFFERS IT?</div>
  <ul class="mini-offers"><li>Most Superannuation Funds</li><li>Some Employers</li><li>General Insurance Companies</li><li>Some Private Health Funds</li><li>Life Insurance Companies</li></ul>
  <div class="mini-band">TIPS AND TRAPS</div>
  <ul class="mini-tips">
    <li>Ensure Policy <b>covers all illnesses and injuries</b>, not just accidents.</li>
    <li><b>Review what the policy doesn't cover "Exclusions"</b>. Standard exclusions include self-inflicted acts and pregnancy related illnesses.</li>
    <li><b>Understand the definitions of "Total and Partial Disability"</b> so you know when you can claim.</li>
    <li>Look to <b>purchase "Long Term" Life Insurance</b> if you will hold the policy for a number of years.</li>
    <li>Ensure the contract is <b>guaranteed to be renewed</b> if you pay your premiums until expiry age.</li>
    <li>Paying the premiums yourself will generally enable you to <b>claim a tax deduction</b>.</li>
  </ul>
  <div class="mini-band">WHEN TO CALL A PROFESSIONAL ADVISOR?</div>
  <p class="mini-text">If you need help:</p>
  <ul class="mini-help"><li>Comparing premiums</li><li>Reviewing &amp; comparing policy terms and conditions</li><li>Matching a policy to suit your occupation</li><li>Deciding on the appropriate Waiting Periods and Benefit Periods</li><li>Purchasing "Long Term" Life Insurance</li></ul>
  <p class="mini-text" style="margin-top:0">If you want to ensure that you have someone assisting you if a claim is ever needed to be made.<br>If your financial affairs are complex due to being self employed or a high income earner.</p>
  <p class="mini-disc">The information provided on this Fact Sheet is general advice only so does not take into account your objective, financial situation and needs.</p>
  <p class="brand" style="margin-top:6px">Halvorsen Brightwick<br>Financial Services</p>
</section>

<section class="mini" style="top:672px">
  <h2 class="mini-title">BUYING LIFE INSURANCE</h2>
  <div class="mini-photo" role="img" aria-label="Photo of a smiling family with the words Life Insurance" style="background:linear-gradient(90deg,#c99a73,#e8c9a8 40%,#f3ece4 65%,#ffffff)"></div>
  <div class="mini-band">HOW MUCH DO I NEED?</div>
  <table class="mini-table">
    <tr><th>Need</th><th>Amount</th></tr>
    <tr><td>Repaying Debts</td><td>$</td></tr>
    <tr><td>Funeral Expenses</td><td>$</td></tr>
    <tr><td>Replacing your Income</td><td>$</td></tr>
    <tr><td>Others</td><td>$</td></tr>
    <tr class="total"><td>Total</td><td>$</td></tr>
  </table>
  <div class="mini-band">WHO OFFERS IT?</div>
  <ul class="mini-offers"><li>Most Superannuation Funds</li><li>Some Employers</li><li>General Insurance Companies</li><li>Some Private Health Funds</li><li>Life Insurance Companies</li></ul>
  <div class="mini-band">TIPS AND TRAPS</div>
  <ul class="mini-tips">
    <li>Ensure contract <b>covers all causes of death</b>, not just accidents.</li>
    <li>Review exclusions. The only standard industry exclusion is "suicide within first 13 months of policy inception or reinstatement".</li>
    <li>Look to <b>purchase "Long Term" Life Insurance</b> if you will hold the policy for a number of years.</li>
    <li>Ensure the contract is <b>guaranteed to be renewed</b> if you pay your premiums until expiry age.</li>
    <li>If purchased through Super, your <b>beneficiaries may be liable for a tax bill</b> in the event of a claim.</li>
  </ul>
  <div class="mini-band">WHEN TO CALL A PROFESSIONAL ADVISOR?</div>
  <p class="mini-text">If you need help:</p>
  <ul class="mini-help"><li>Comparing premiums on policies</li><li>Reviewing wording of insurance contracts</li><li>Structuring your policies to get a tax deduction</li><li>Avoiding tax on claim proceeds</li><li>Purchasing "Long Term" Life Insurance</li></ul>
  <p class="mini-text" style="margin-top:0">If you want to ensure that you have someone assisting your family if a claim is ever needed to be made</p>
  <p class="mini-disc">The information provided on this Fact Sheet is general advice only and does not consider your personal needs.</p>
  <p class="brand" style="margin-top:5px">Halvorsen Brightwick<br>Financial Services</p>
</section>

</body>
</html>
```